Subway/Bus ad sign for a paid research study

We are looking for someone who can help design an effective advertisement sign for a paid research study. The ad will be displayed in subway stations/bus. The study involves fMRI and is conducted by a laboratory in the University of Kestrelmoor.

We prefer ppt images so we could edit. Dimensions should be 46”h x 60”w, but may vary in the final version depending on our needs.

The way we would like to choose the final design is by running a pretest on friendvale to pick the most attractive ad. Your submission would mean that you consent with this process.

Thank you for your consideration.

Target Market(s)

age 18-64, philadelphia

Requirements
Must have
• The ad must include the following information (we encourage you to come up with better/more catchy slogans)
• - We are looking for participants for a research study
• - This fMRI study is conducted by researchers at University of Kestrelmoor
• - Email KmoorLB7@psy.kestrelmoor-edu.org to see if you are eligible
• - University of Kestrelmoor Logo
• The ad may include the following information
• - Participants get paid up to $190
Nice to have
• original attractive illustrations are highly encouraged.
Should not have
• It seems like brain photos tend to scare people away. Maybe you could focus on using survey-related images or illustrated images of the brain (vs. fMRI scans).

```html
<!DOCTYPE html>
<html lang="en">
<head>
<meta charset="utf-8">
<title>fMRI Study Transit Ad</title>
<link href="https://fonts.googleapis.com/css2?family=Oswald:wght@400;500&display=swap" rel="stylesheet">
<style>
  :root {
    --red: #e07a7f;
    --pink-light: #f6d2d2;
    --mauve: #e2bfd3;
    --lavender: #c3c1da;
    --slate: #bac6d2;
    --mist: #e3e8ec;
    --white: #ffffff;
    --mint: #deeee1;
    --rail: rgba(80, 80, 80, 0.42);
    --ink: #1d1d1f;
    --coin: #add67f;
    --coin-ink: #1f5a2d;
    --brain: #c0636b;
    --crest: #8e2634;
  }
  html, body {
    margin: 0;
    padding: 0;
    overflow: hidden;
    background: #ffffff;
  }
  .ad {
    position: relative;
    width: 1200px;
    height: 302px;
    overflow: hidden;
    font-family: "Oswald", "Arial Narrow", sans-serif;
    color: var(--ink);
  }
  .ad-bands {
    position: absolute;
    inset: 0;
    display: block;
  }
  .headline {
    position: absolute;
    margin: 0;
    font-weight: 500;
    font-size: 31px;
    line-height: 38px;
    text-align: center;
    letter-spacing: 0.6px;
    transform: translateX(-50%);
    white-space: nowrap;
  }
  .headline--scanned { left: 73px; top: 114px; }
  .headline--paid { left: 409px; top: 114px; }
  .headline--study { left: 729px; top: 114px; }
  .headline--at { left: 839px; top: 133px; }
  .brain-illustration {
    position: absolute;
    left: 172px;
    top: 90px;
    width: 126px;
    height: 118px;
    border-radius: 50% 50% 44% 48%;
    background: radial-gradient(circle at 45% 40%, #d0757c, var(--brain));
  }
  .coin {
    position: absolute;
    left: 449px;
    top: 92px;
    width: 112px;
    height: 112px;
    box-sizing: border-box;
    border-radius: 50%;
    background: var(--coin);
    border: 4px solid var(--white);
    display: flex;
    align-items: center;
    justify-content: center;
    font-size: 74px;
    font-weight: 500;
    color: var(--coin-ink);
    line-height: 1;
  }
  .institution {
    position: absolute;
    left: 926px;
    top: 114px;
    transform: translateX(-50%);
    display: flex;
    flex-direction: column;
    align-items: center;
    gap: 12px;
  }
  .institution-name {
    font-size: 31px;
    line-height: 34px;
    font-weight: 500;
    letter-spacing: 0.6px;
  }
  .institution-mark {
    width: 48px;
    height: 48px;
    background: var(--crest);
  }
  .contact {
    position: absolute;
    left: 1092px;
    top: 104px;
    transform: translateX(-50%);
    margin: 0;
    text-align: center;
    white-space: nowrap;
  }
  .contact-label {
    display: block;
    font-size: 31px;
    line-height: 38px;
    font-weight: 500;
    letter-spacing: 0.6px;
  }
  .contact-email {
    display: block;
    margin-top: 6px;
    font-size: 19px;
    line-height: 24px;
    font-weight: 500;
  }
</style>
</head>
<body>
  <main class="ad">
    <svg class="ad-bands" width="1200" height="302" viewBox="0 0 1200 302" aria-hidden="true">
      <rect width="1200" height="302" fill="var(--mint)"/>
      <circle cx="662" cy="151" r="320" fill="var(--white)"/>
      <circle cx="556" cy="151" r="320" fill="var(--mist)"/>
      <circle cx="489" cy="151" r="320" fill="var(--slate)"/>
      <circle cx="293" cy="151" r="320" fill="var(--lavender)"/>
      <circle cx="213" cy="151" r="320" fill="var(--mauve)"/>
      <circle cx="27" cy="151" r="320" fill="var(--pink-light)"/>
      <circle cx="-178" cy="151" r="320" fill="var(--red)"/>
      <rect class="rail rail--top" x="0" y="0" width="1200" height="13" fill="var(--rail)"/>
      <rect class="rail rail--bottom" x="0" y="289" width="1200" height="13" fill="var(--rail)"/>
    </svg>

    <h2 class="headline headline--scanned">GET<br>SCANNED</h2>
    <div class="brain-illustration" role="img" aria-label="Illustrated pink cartoon brain"></div>

    <h2 class="headline headline--paid">GET<br>PAID</h2>
    <div class="coin" aria-hidden="true">$</div>

    <h2 class="headline headline--study">FOR AN<br>fMRI STUDY</h2>

    <h2 class="headline headline--at">AT</h2>

    <div class="institution">
      <span class="institution-name">KMOOR</span>
      <span class="institution-mark" aria-hidden="true"></span>
    </div>

    <p class="contact">
      <span class="contact-label">EMAIL</span>
      <span class="contact-email">KmoorLB7@psy.<br>kestrelmoor-edu.org</span>
    </p>
  </main>
</body>
</html>
```